Business Card Design Project

We need a business card design for a new construction company called 'KVORA HOLDINGS PTY.LTD' We run a construction based company for high end market homes in melbourne, we want something that looks professional and eye catching.The card needs to have a strong design to it something modern as the company name explains "kvora." The final design should communicate professionalism and a strong image to our customers on the quality of our work.
On the business card i need
Name: Marek Tollaway
Mob:0417295041
Email:kvora.holdings@mailbrook.example
Domestic/Residential/Commercial
Industry/Entity Type
Construction
Look and feel
Each slider illustrates characteristics of the customer's brand and the style your logo design should communicate.

```html
<!DOCTYPE html>
<html lang="en">
<head>
<meta charset="utf-8">
<title>Kvora Holdings – Business Card</title>
<link rel="stylesheet" href="https://fonts.googleapis.com/css2?family=Questrial&family=Open+Sans:wght@400&display=swap">
<style>
  :root {
    --stage: #3a3a3c;
    --card: #e3e5e3;
    --card-edge: #d6d9d6;
    --band: #f4f5f4;
    --ink: #231f20;
    --accent: #e8322b;
    --label: #111111;
    --label-bg: #ffffff;
  }
  * { box-sizing: border-box; margin: 0; padding: 0; }
  html, body { width: 1200px; height: 510px; overflow: hidden; }
  body {
    background: var(--stage);
    font-family: "Questrial", sans-serif;
    color: var(--ink);
    position: relative;
  }
  .card {
    position: absolute;
    top: 73px;
    width: 569px;
    height: 322px;
    background: linear-gradient(135deg, var(--card) 0%, #eceeec 50%, var(--card-edge) 100%);
    overflow: hidden;
  }
  .card--front { left: 26px; }
  .card--back { left: 610px; }

  .side-label {
    position: absolute;
    top: 400px;
    width: 569px;
    height: 50px;
    line-height: 50px;
    text-align: center;
    font-family: "Open Sans", sans-serif;
    font-size: 38px;
    color: var(--label);
    background: var(--label-bg);
  }
  .side-label--front { left: 26px; }
  .side-label--back { left: 610px; }

  /* Front */
  .front-band {
    position: absolute;
    left: 0; right: 0;
    top: 63px;
    height: 200px;
    background: var(--band);
    box-shadow: 0 6px 10px rgba(0,0,0,0.12);
  }
  .brand {
    position: absolute;
    display: flex;
    flex-direction: column;
    align-items: center;
  }
  .brand__name {
    font-family: "Questrial", sans-serif;
    color: var(--ink);
    line-height: 1;
  }
  .brand__entity {
    font-family: "Questrial", sans-serif;
    color: var(--accent);
    white-space: nowrap;
  }
  .brand--front { left: 0; right: 0; top: 72px; }
  .brand--front .brand__name { font-size: 150px; letter-spacing: 4px; }
  .brand--front .brand__entity { font-size: 19px; letter-spacing: 11.5px; margin-top: -2px; margin-left: 11px; }

  /* Back */
  .brand--back { right: 22px; top: 8px; }
  .brand--back .brand__name { font-size: 76px; letter-spacing: 2px; }
  .brand--back .brand__entity { font-size: 10px; letter-spacing: 5.5px; margin-top: 0; }

  .contact {
    position: absolute;
    left: 14px;
    top: 155px;
    list-style: none;
    font-size: 24px;
    line-height: 33px;
  }
  .contact__key { color: var(--accent); }

  .services-band {
    position: absolute;
    left: 0; right: 0;
    top: 263px;
    height: 59px;
    background: var(--band);
    box-shadow: 0 -8px 12px rgba(0,0,0,0.10);
    display: flex;
    align-items: center;
    justify-content: center;
    font-size: 24px;
  }
  .services-band__divider { color: var(--accent); }
</style>
</head>
<body>
  <section class="card card--front" aria-label="Card front">
    <div class="front-band"></div>
    <div class="brand brand--front">
      <span class="brand__name">kvora</span>
      <span class="brand__entity">HOLDINGS PTY.LTD</span>
    </div>
  </section>

  <section class="card card--back" aria-label="Card back">
    <div class="brand brand--back">
      <span class="brand__name">kvora</span>
      <span class="brand__entity">HOLDINGS PTY.LTD</span>
    </div>
    <ul class="contact">
      <li><span class="contact__key">Name:</span> Marek Tollaway</li>
      <li><span class="contact__key">Mob:</span>0417295041</li>
      <li><span class="contact__key">Email:</span>kvora.holdings@mailbrook.example</li>
    </ul>
    <div class="services-band">
      Domestic<span class="services-band__divider">/</span>Residential<span class="services-band__divider">/</span>Commercial
    </div>
  </section>

  <div class="side-label side-label--front">front</div>
  <div class="side-label side-label--back">back</div>
</body>
</html>
```